Tri-Fold Behavioral Health (Addiction) Agency Brochure

We need an updated and refreshed brochure design for our Residential Treatment Facilities. These facilities provide residential comprehensive treatment for those struggling with drug and alcohol addiction along with those who are dually diagnosed with mental health issues as well. We are starting with this brochure but plan to have our other brochures "match" the design and will submit that following completion of this design. I have attached a "Brochure Areas" document that is numbered and corresponds to the brochure areas of our current brochure. We have modified the wording in each of these areas so the wording in the attached word document is what needs to go on the design (not the words in the attached pictures of our current brochure). We want something that is a professional design look. The front page of the brochure needs to have our main agency Logo/Name: Maple Hollow Behavioral Health Partners (logo attached). The back page we would like to have the two locations listed with the address (possible map if able). The first is called: The Harbor at Maple Hollow - located at 7214 Tolliver Lane, Frazeysburg OH 43829. The Second Facility is called: The Brennick at Maple Hollow - located at 618 Garvin St, Zanesville OH 43708. I have also attached some pictures of our facilities that can be used. They all don't have to be used and we would still like some stock photos of "people" or group counseling, etc.

Requirements
Must have
• Need final design file to be publisher or word along with pdf and or other print type file.
Nice to have
• I have also attached the current booth design photo that we are using to possibly match design look.

```html
<!DOCTYPE html>
<html lang="en">
<head>
<meta charset="utf-8">
<title>Maple Hollow Residential Treatment – Inside Panel</title>
<link href="https://fonts.googleapis.com/css2?family=Playfair+Display:ital,wght@0,400;1,400&family=Arimo:wght@400&display=swap" rel="stylesheet">
<style>
:root{
  --green:#2d8f22;
  --teal:#1b6f86;
  --ink:#111111;
  --paper:#ffffff;
  --haze:#d9d9d9;
  --garden-a:#6f9a4a;
  --garden-b:#c9c3b4;
  --sky-a:#b9bec4;
  --sky-b:#6e8a4a;
  --people-a:#a9b3c2;
  --people-b:#6b5a52;
  --fern-a:#1f3a2a;
  --fern-b:#3f7a3e;
}
*{margin:0;padding:0;box-sizing:border-box}
html,body{width:1200px;height:927px;overflow:hidden;background:var(--paper)}
.canvas{position:relative;width:1200px;height:927px;overflow:hidden;background:var(--paper)}
.panel-spread{position:absolute;left:0;top:0;width:1056px;height:816px;transform:scale(1.13636);transform-origin:0 0;font-family:"Arimo",Arial,sans-serif;color:var(--ink)}
.photo{position:absolute;border-radius:50%;border-style:solid;border-width:7px}
.photo--garden{left:-70px;top:-75px;width:400px;height:400px;border-color:var(--green);background:linear-gradient(160deg,var(--garden-b),var(--garden-a) 65%)}
.photo--firepit{left:345px;top:2px;width:357px;height:357px;border-color:var(--teal);background:linear-gradient(180deg,var(--sky-a) 0 48%,var(--sky-b) 62%,#9a8a72 100%)}
.photo--group{left:712px;top:-55px;width:392px;height:392px;border-color:var(--green);background:linear-gradient(120deg,var(--people-a),var(--people-b))}
.photo--fern{left:340px;top:690px;width:350px;height:350px;border-color:var(--teal);background:radial-gradient(circle at 50% 40%,var(--fern-b),var(--fern-a) 70%)}
.backdrop{position:absolute;border-radius:45%;background:radial-gradient(ellipse at 50% 50%,var(--haze) 0,rgba(217,217,217,.55) 55%,rgba(217,217,217,0) 75%)}
.backdrop--left{left:-10px;top:320px;width:360px;height:500px}
.backdrop--right{left:690px;top:300px;width:360px;height:516px}
.heading{position:absolute;font-family:"Playfair Display",Georgia,serif;font-weight:400;line-height:1;white-space:nowrap}
.heading__lead{font-size:44px}
.heading__main{font-size:58px;font-style:italic}
.heading--green{color:var(--green)}
.heading--teal{color:var(--teal)}
.body-copy{position:absolute;text-align:center;font-size:16.2px;line-height:23px;white-space:nowrap}
.body-copy p+p{margin-top:23px}
.body-copy--small{font-size:15px;line-height:20.6px}
.feature-list{position:absolute;list-style:none;font-size:13.2px;line-height:19px;white-space:nowrap}
.feature-list li::before{content:"•";margin-right:6px}
</style>
</head>
<body>
<div class="canvas">
 <div class="panel-spread">
  <div class="backdrop backdrop--left" role="img" aria-label="Faded evergreen tree backdrop"></div>
  <div class="backdrop backdrop--right" role="img" aria-label="Faded evergreen tree backdrop"></div>

  <div class="photo photo--garden" role="img" aria-label="Photo of the facility entrance with garden and steps"></div>
  <div class="photo photo--firepit" role="img" aria-label="Photo of outdoor fire pit with wooden chairs under a cloudy sky"></div>
  <div class="photo photo--group" role="img" aria-label="Photo of a group counseling conversation"></div>
  <div class="photo photo--fern" role="img" aria-label="Photo of green fern leaves"></div>

  <div class="heading heading--green heading__lead" style="left:8px;top:338px">The</div>
  <div class="heading heading--green heading__main" style="left:63px;top:370px">Experience</div>
  <div class="body-copy" style="left:0;top:439px;width:326px">
   <p>Residential Treatment at Maple Hollow<br>offers intensive structured treatment<br>services for men and women suffering from<br>substance abuse disorders in a 24-hour<br>medically monitored Long-term residential<br>treatment facility.</p>
   <p>Our treatment facilities offer clients the<br>ability to feel welcomed, accepted and<br>supported in a retreat like setting. Our<br>multi-disciplinary team consists of<br>Physicians, Therapists, Nurses, Case<br>Managers, and other Recovery Support<br>Specialists, allowing for each individual’s<br>physical, social, mental, and emotional<br>development.</p>
  </div>

  <div class="heading heading--teal heading__lead" style="left:357px;top:343px">Dual</div>
  <div class="heading heading--teal heading__main" style="left:432px;top:378px">Diagnosis</div>
  <div class="body-copy" style="left:356px;top:440px;width:324px">
   <p>It is an unfortunate reality that many<br>individuals who struggle with addiction are<br>also faced with mental illness. Our<br>residential treatment programs support<br>dually-diagnosed individuals by providing<br>onsite psychiatric evaluations, regular<br>psychiatric follow-ups, medication<br>management, and therapy services aimed<br>at treating these symptoms as a part of the<br>client’s individualized treatment plan.</p>
  </div>

  <div class="heading heading--green heading__lead" style="left:726px;top:338px">Our</div>
  <div class="heading heading--green heading__main" style="left:783px;top:378px">Programs</div>
  <div class="body-copy body-copy--small" style="left:704px;top:445px;width:352px">
   <p>Residential treatment programing provides<br>comprehensive treatment for those struggling with<br>drug and alcohol addiction along with those who<br>are dually diagnosed with mental health issues as<br>well. Residents will be able to experience an<br>evidence-based program model inclusive of:</p>
  </div>
  <ul class="feature-list" style="left:705px;top:588px">
   <li>Comprehensive Evaluations</li>
   <li>Treatment Team Collaboration</li>
   <li>Medication Management</li>
  </ul>
  <ul class="feature-list" style="left:912px;top:588px">
   <li>Aftercare Planning</li>
   <li>Individual Therapy</li>
   <li>Family Therapy</li>
   <li>Group Therapy</li>
  </ul>

  <div class="heading heading--teal heading__main" style="left:777px;top:656px">Groups</div>
  <ul class="feature-list" style="left:705px;top:727px">
   <li>Psychoeducational</li>
   <li>Psychotherapy</li>
   <li>Health &amp; Wellness</li>
   <li>Independent Living Skills</li>
  </ul>
  <ul class="feature-list" style="left:887px;top:727px">
   <li>Peer-Led (AA/NA)</li>
   <li>Grief &amp; Loss</li>
   <li>Codependency</li>
   <li>Stress Management</li>
  </ul>
 </div>
</div>
</body>
</html>
```